Local Flower Farm Needs Business Card Design

I need business cards designed for a flower farm based in Eudora, Kansas.
Business Info:
We are a local cut flower farm located in Eudora, Kansas, founded by Darla Hoffstrom. What started as a passion for agriculture and search for more joy in daily life has blossomed into a small business dedicated to providing the community with beautiful, fresh, and sustainable flowers. We specialize in local, seasonal blooms, ensuring that every petal reflects the care and dedication we pour into our craft. Our mission is to deliver the highest quality flowers directly to our customers through local farmers markets and to florists who share our commitment to sustainability. Join us in celebrating the beauty of nature, one bloom at a time!
Contact Details:
Darla Hoffstrom
Owner
Phone 913-555-0147
Facebook: Lorabelle Quinn Blossoms
Instagram: @LorabelleQuinnBlossoms
Website: LorabelleQuinnBlossoms.example
Target Market(s)
Wholesale to Florists and Direct to Consumer via Farmers Market
Industry/Entity Type
Florist, Farm
Contact Information for Business Card
Name, Contact Info, Logo
Look and feel

```html
<!DOCTYPE html>
<html lang="en">
<head>
<meta charset="utf-8">
<title>Lorabelle Quinn Blossoms – Business Card</title>
<link href="https://fonts.googleapis.com/css2?family=Montserrat:wght@400;700&display=swap" rel="stylesheet">
<style>
  :root {
    --backdrop: #cfd4d3;
    --paper: #efefec;
    --ink: #0f2e2e;
    --ink-soft: #3d4a4a;
    --rule: #9aa3a2;
  }
  html, body {
    margin: 0;
    padding: 0;
    width: 1200px;
    height: 881px;
    overflow: hidden;
    background: var(--backdrop);
    font-family: "Montserrat", sans-serif;
    color: var(--ink);
  }
  .sheet {
    width: 1200px;
    height: 881px;
    display: flex;
    flex-direction: column;
    align-items: center;
    justify-content: center;
    gap: 48px;
  }
  .card {
    width: 640px;
    height: 366px;
    background: var(--paper);
    box-shadow: 0 6px 18px rgba(0,0,0,0.10);
    box-sizing: border-box;
    position: relative;
  }
  .card--front {
    display: flex;
    align-items: center;
    padding: 0 40px;
  }
  .brand {
    width: 200px;
    display: flex;
    flex-direction: column;
    align-items: center;
    gap: 14px;
  }
  .brand__dot {
    width: 22px;
    height: 22px;
    border: 1.5px solid var(--ink);
    border-radius: 50%;
  }
  .brand__name {
    font-weight: 700;
    font-size: 17px;
    line-height: 1.35;
    letter-spacing: 0.12em;
    text-transform: uppercase;
    text-align: center;
    color: var(--ink);
  }
  .divider {
    width: 1px;
    align-self: stretch;
    margin: 52px 34px;
    background: var(--rule);
  }
  .contact__name {
    font-weight: 700;
    font-size: 27px;
    margin: 0;
    line-height: 1.1;
  }
  .contact__role {
    font-size: 15px;
    color: var(--ink-soft);
    margin: 2px 0 14px;
  }
  .contact__list {
    list-style: none;
    margin: 0;
    padding: 0;
    font-size: 14px;
    line-height: 1.45;
    color: var(--ink-soft);
  }
  .contact__label {
    font-weight: 700;
    color: var(--ink);
  }
  .card--back {
    display: flex;
    align-items: center;
    justify-content: center;
  }
  .card--back .brand {
    width: 300px;
  }
  .card--back .brand__name {
    font-size: 22px;
  }
  .card--back .brand__dot {
    width: 28px;
    height: 28px;
  }
</style>
</head>
<body>
<main class="sheet">
  <section class="card card--front">
    <div class="brand">
      <span class="brand__dot"></span>
      <span class="brand__name">Lorabelle Quinn<br>Blossoms</span>
    </div>
    <div class="divider"></div>
    <div class="contact">
      <h1 class="contact__name">Darla Hoffstrom</h1>
      <p class="contact__role">Owner</p>
      <ul class="contact__list">
        <li><span class="contact__label">Facebook:</span> Lorabelle Quinn Blossoms</li>
        <li><span class="contact__label">Instagram:</span> @LorabelleQuinnBlossoms</li>
        <li><span class="contact__label">Website:</span> LorabelleQuinnBlossoms.example</li>
      </ul>
    </div>
  </section>
  <section class="card card--back">
    <div class="brand">
      <span class="brand__dot"></span>
      <span class="brand__name">Lorabelle Quinn<br>Blossoms</span>
    </div>
  </section>
</main>
</body>
</html>
```